Business is called "Pelton Ledger". Accounting and tax services.

I need a flyer for my new business "Pelton Ledger". I am an individual accountant working for himself on the Sunshine Coast in Queensland Australia. I would like to see designs that communicate reliability and trust. I believe my point of difference is that I am always available to my clients and I will cap my number of clients to ensure I can service them properly. Accountants in general seem to have a bad reputation for not responding to clients in a timely fashion, whether by email or phone. This is where I intend to differentiate myself. I have included my business card for ideas on colour and for contact information. I have also included some logo's that should go on the flyer. With the QLA logo, the words "Pelton Ledger is a QLA Business" needs to be written either above, below or to the right hand side (as per the business card).

Target Market(s)

Small business owners and individuals requiring taxation and financials

Industry/Entity Type

Public Accounting

Font styles to use
Serif

Requirements
Must have
• Supplied logo's, accounting style pictures etc
Services: Small Business Taxation
Company & Trust Tax Returns
Rental Property Returns
Capital Gains Tax
Individual Tax Returns
BAS and IAS lodgements
Nice to have
• Needs to convey a sense of being reliable and responds to clients quickly.
Should not have
• My name

```html
<!DOCTYPE html>
<html lang="en">
<head>
<meta charset="utf-8">
<title>Pelton Ledger – Flyer</title>
<link rel="stylesheet" href="https://fonts.googleapis.com/css2?family=Merriweather:wght@400;700&family=Montserrat:wght@700&family=Source+Serif+4:wght@600;700&display=swap">
<style>
  :root {
    --page-bg: #e4e2e1;
    --paper: #ffffff;
    --ink: #222222;
    --band: #425eaa;
    --overlay: rgba(112, 124, 196, 0.82);
    --white: #ffffff;
    --badge-fill: #d9d9d9;
  }
  * { box-sizing: border-box; margin: 0; padding: 0; }
  html, body {
    width: 1200px; height: 1200px; overflow: hidden;
    background: var(--page-bg);
  }
  .flyer {
    position: absolute; left: 176px; top: 0;
    width: 848px; height: 1200px;
    background: var(--paper);
    font-family: "Merriweather", Georgia, serif;
    color: var(--ink);
    overflow: hidden;
  }

  /* Header */
  .brand {
    position: absolute; left: 51px; top: 24px; width: 182px;
    text-align: center;
  }
  .brand-dot {
    display: block; margin: 0 auto;
    width: 68px; height: 68px; border-radius: 50%;
    border: 2px solid var(--ink);
  }
  .brand-name {
    display: block; margin-top: 14px;
    font-family: "Merriweather", Georgia, serif; font-weight: 400;
    font-size: 17px; letter-spacing: 3px; color: var(--ink);
    white-space: nowrap;
  }
  .call-label {
    position: absolute; left: 353px; top: 22px; width: 443px;
    text-align: center;
    font-family: "Source Serif 4", Georgia, serif; font-weight: 700;
    font-size: 24px; letter-spacing: 0.5px;
  }
  .call-number {
    position: absolute; left: 340px; top: 48px; width: 470px;
    text-align: center;
    font-family: "Source Serif 4", Georgia, serif; font-weight: 700;
    font-size: 78px; line-height: 1; color: var(--ink);
    white-space: nowrap;
  }

  /* Hero */
  .hero-photo {
    position: absolute; left: 0; top: 141px; width: 848px; height: 423px;
    background:
      linear-gradient(90deg, transparent 0 80%, #1b1b1d 88% 100%),
      linear-gradient(180deg, transparent 0 80%, rgba(20,20,22,0.9) 95%),
      linear-gradient(135deg, #dcdcdc 0%, #eeeae4 40%, #d8d4cf 70%, #bdbab6 100%);
  }
  .hero-panel {
    position: absolute; left: 0; top: 243px; width: 675px; height: 219px;
    background: var(--overlay);
  }
  .hero-title {
    position: absolute; left: 52px; top: 253px;
    font-family: "Montserrat", Arial, sans-serif; font-weight: 700;
    font-size: 52px; line-height: 66px; color: var(--white);
    white-space: nowrap;
  }

  /* Bands */
  .band {
    position: absolute; left: 0; width: 848px;
    background: var(--band); color: var(--white); text-align: center;
  }
  .about { top: 564px; height: 198px; }
  .services { top: 765px; height: 182px; }
  .band-title {
    font-weight: 700; font-size: 27px; line-height: 1;
  }
  .about .band-title { margin-top: 15px; }
  .about-text {
    margin: 10px auto 0; width: 745px;
    font-weight: 700; font-size: 18.6px; line-height: 25.5px;
  }
  .services .band-title { margin-top: 15px; }
  .service-list {
    position: absolute; top: 62px; list-style: none; text-align: left;
    font-size: 23.5px; line-height: 32px;
  }
  .service-list.left { left: 63px; }
  .service-list.right { left: 409px; }
  .service-list li { display: flex; align-items: center; white-space: nowrap; }
  .service-list svg { width: 16px; height: 17px; margin-right: 11px; flex: none; }

  /* Expertise */
  .expertise-pill {
    position: absolute; left: 312px; top: 965px; width: 220px; height: 38px;
    border-radius: 19px; background: var(--band); color: var(--white);
    font-weight: 700; font-size: 24px; line-height: 38px; text-align: center;
  }
  .partner-qla {
    position: absolute; left: 175px; top: 1022px; width: 193px; text-align: center;
  }
  .partner-qla .name {
    display: block; height: 64px; line-height: 64px;
    font-weight: 700; font-size: 34px; color: var(--ink);
  }
  .partner-qla .caption {
    margin-top: 4px; font-size: 11.5px; white-space: nowrap;
  }
  .partner-tally {
    position: absolute; left: 430px; top: 1032px; width: 100px; height: 54px;
    line-height: 54px; text-align: center;
    font-weight: 700; font-size: 24px; color: var(--ink);
  }
  .partner-badge {
    position: absolute; left: 588px; top: 1012px; width: 80px; text-align: center;
  }
  .partner-badge .seal {
    width: 68px; height: 68px; margin: 0 auto; border-radius: 50%;
    background: var(--badge-fill);
  }
  .partner-badge .caption {
    margin-top: 5px; font-family: Arial, Helvetica, sans-serif; font-size: 8.5px; line-height: 11px;
  }

  /* Footer */
  .footer { top: 1117px; height: 83px; }
  .contact {
    position: absolute; top: 30px; display: flex; align-items: center;
    font-size: 21px; color: var(--white); white-space: nowrap;
  }
  .contact.email { left: 112px; }
  .contact.web { left: 464px; top: 27px; }
  .contact svg { flex: none; margin-right: 18px; }
</style>
</head>
<body>
<main class="flyer">
  <header>
    <div class="brand">
      <span class="brand-dot"></span>
      <span class="brand-name">PELTON LEDGER</span>
    </div>
    <p class="call-label">CALL FOR AN APPOINTMENT</p>
    <p class="call-number">0412 555 018</p>
  </header>

  <section>
    <div class="hero-photo" role="img" aria-label="Overhead photo of tax forms, folders, a calculator and a pen on a white timber desk, with a person's arm and knees at the edges"></div>
    <div class="hero-panel"></div>
    <h1 class="hero-title">Looking for<br>A Fast &amp; Reliable<br>Accounting Service?</h1>
  </section>

  <section class="band about">
    <h2 class="band-title">About Us</h2>
    <p class="about-text">We Are One Of Australia’s Best Tax Accounting Firms, That Have Helped Thousands Of Freelancers, Contractors, E-Commerce And Small To Medium Sized Businesses To Flourish As A Result. We Help With All Aspects Of Accounting, Tax And Business Growth Strategies Across A Range Of Different Industries.</p>
  </section>

  <section class="band services">
    <h2 class="band-title">Our Services</h2>
    <ul class="service-list left">
      <li><svg viewBox="0 0 16 17"><path d="M1 1 L15 8.5 L1 16 L5 8.5 Z" fill="#fff"/></svg>Small Business Taxation</li>
      <li><svg viewBox="0 0 16 17"><path d="M1 1 L15 8.5 L1 16 L5 8.5 Z" fill="#fff"/></svg>Rental Property Returns</li>
      <li><svg viewBox="0 0 16 17"><path d="M1 1 L15 8.5 L1 16 L5 8.5 Z" fill="#fff"/></svg>Individual Tax Returns</li>
    </ul>
    <ul class="service-list right">
      <li><svg viewBox="0 0 16 17"><path d="M1 1 L15 8.5 L1 16 L5 8.5 Z" fill="#fff"/></svg>Capital Gains Tax</li>
      <li><svg viewBox="0 0 16 17"><path d="M1 1 L15 8.5 L1 16 L5 8.5 Z" fill="#fff"/></svg>BAS and IAS lodgements</li>
      <li><svg viewBox="0 0 16 17"><path d="M1 1 L15 8.5 L1 16 L5 8.5 Z" fill="#fff"/></svg>Company &amp; Trust Tax Returns</li>
    </ul>
  </section>

  <section class="expertise">
    <h2 class="expertise-pill">Our Expertise</h2>
    <div class="partner-qla">
      <span class="name">QLA</span>
      <p class="caption">Pelton Ledger is a QLA Business</p>
    </div>
    <div class="partner-tally">Tallyo</div>
    <div class="partner-badge">
      <div class="seal"></div>
      <p class="caption">Tax agent<br>51920387</p>
    </div>
  </section>

  <footer class="band footer">
    <p class="contact email">
      <svg width="28" height="20" viewBox="0 0 28 20"><rect x="1" y="1" width="26" height="18" fill="none" stroke="#fff" stroke-width="2"/><path d="M1 1 L14 11 L27 1" fill="none" stroke="#fff" stroke-width="2"/></svg>
      hello@peltonledger.com.au
    </p>
    <p class="contact web">
      <svg width="30" height="30" viewBox="0 0 30 30"><circle cx="15" cy="15" r="13.5" fill="none" stroke="#fff" stroke-width="2"/><ellipse cx="15" cy="15" rx="6" ry="13.5" fill="none" stroke="#fff" stroke-width="1.6"/><path d="M2 15 H28 M4 8 H26 M4 22 H26" stroke="#fff" stroke-width="1.6"/></svg>
      www.peltonledger.com.au
    </p>
  </footer>
</main>
</body>
</html>
```